Trifold Brochure needed for Elm Path Counseling

Hi! We need to have a trifold brochure made.

We would like to see brochure designs that use our logo colors, which are khaki, chocolate brown, and gray.

The brochure should be a modern design and please use your creativity.

Brochure is a trifold brochure, size is 8.5 x 11 and full color.

The following attachment has the content to be used in the trifold brochure, as well as some possible pictures. I have also attached our logo.

We would like to use file #2 for sure (picture number 27193540) and add the quote from her...

"At first, I was reluctant about going to ElmPath. Once I got there, I was glad I went. I learned a lot and was treated like family the whole time." Maren Colby

Requirements
Must have
• Our logo
• Information should be listed exactly as the attached document
• You must stick with our logo colors

```html
<!DOCTYPE html>
<html lang="en">
<head>
<meta charset="utf-8">
<title>Elm Path Counseling – Trifold Brochure</title>
<link rel="stylesheet" href="https://fonts.googleapis.com/css2?family=Open+Sans:wght@400;600&family=Didact+Gothic&display=swap">
<style>
  :root {
    --backdrop: #5b5b5b;
    --paper: #ffffff;
    --chocolate: #6b3f1a;
    --chocolate-deep: #4e2c10;
    --khaki: #c49a6c;
    --khaki-light: #dcc3a3;
    --cream: #efe3d3;
    --ink: #2b2420;
    --gray: #8a8a8a;
  }
  * { box-sizing: border-box; margin: 0; padding: 0; }
  html, body { width: 1200px; height: 900px; overflow: hidden; }
  body {
    background: var(--backdrop);
    font-family: "Open Sans", Arial, sans-serif;
    color: var(--ink);
  }
  .brochure {
    position: absolute; left: 120px; top: 72px;
    width: 960px; height: 750px;
    display: flex;
    box-shadow: 0 10px 30px rgba(0,0,0,.35);
  }
  .panel { position: relative; width: 320px; height: 750px; overflow: hidden; background: var(--paper); }
  .panel + .panel { border-left: 1px solid rgba(0,0,0,.08); }
  .panel-art { position: absolute; inset: 0; }
  .band-title {
    position: absolute; font-family: "Didact Gothic", sans-serif;
    text-transform: uppercase; font-size: 19px; line-height: 19px; letter-spacing: 1.5px;
    transform-origin: left top;
  }

  /* FAQ panel */
  .faq-title { left: 118px; top: 14px; color: var(--chocolate-deep); transform: rotate(32deg); }
  .faq-list { position: absolute; left: 24px; top: 84px; width: 270px; }
  .faq-item { margin-bottom: 12px; }
  .faq-question {
    color: var(--khaki); font-weight: 600; font-size: 12.5px; line-height: 15px;
    padding-bottom: 4px; border-bottom: 1.5px solid var(--khaki);
    width: 175px; margin-bottom: 6px; white-space: nowrap;
  }
  .faq-question.wide { width: 270px; }
  .faq-answer { font-size: 11.5px; line-height: 15px; }
  .faq-answer small { font-size: 10px; display: block; }
  .faq-item.narrow .faq-answer { width: 145px; }
  .faq-item.narrow .faq-question { color: var(--chocolate-deep); width: 150px; white-space: normal; }
  .photo-patient-ledger { position: absolute; left: 170px; top: 500px; width: 150px; height: 250px;
    background: linear-gradient(180deg, #e9e6e1 0%, #c9c3bb 60%, #a9a39d 100%); }
  .faq-item.narrow { position: absolute; left: 24px; top: 562px; }

  /* Reminders panel */
  .reminder-title { left: 30px; top: 92px; color: var(--cream); transform: rotate(33deg); }
  .reminder-list { position: absolute; left: 22px; top: 270px; width: 280px; color: #fff; }
  .reminder { font-size: 12px; line-height: 17px; padding-bottom: 9px; margin-bottom: 10px;
    border-bottom: 1.5px solid var(--khaki-light); }
  .reminder:last-child { border-bottom: none; }
  .reminder strong { font-weight: 600; }
  .contact strong { font-weight: 600; }
  .mission { position: absolute; left: 22px; top: 562px; width: 290px; }
  .mission p { font-size: 12px; line-height: 19px; }
  .mission .name { font-weight: 600; color: var(--chocolate-deep); }
  .mission .call { margin-top: 26px; color: var(--chocolate); font-weight: 600; font-size: 14px; line-height: 20px; }
  .mission .close { font-family: "Didact Gothic", sans-serif; color: var(--khaki); font-size: 19px; margin-top: 4px; }

  /* Cover panel */
  .photo-couple { position: absolute; inset: 0; }
  .cover-headline { position: absolute; left: 22px; top: 346px; color: #f4ebe0;
    font-family: "Didact Gothic", sans-serif; font-size: 26px; line-height: 36px; }
  .brand { position: absolute; right: 34px; top: 660px; display: flex; align-items: center; gap: 10px; }
  .brand-dot { width: 14px; height: 14px; border-radius: 50%; background: var(--gray); }
  .brand-text { text-align: left; color: var(--chocolate); }
  .brand-name { font-size: 26px; line-height: 28px; font-weight: 400; }
  .brand-sub { font-size: 9px; line-height: 12px; }
</style>
</head>
<body>
<div class="brochure">

  <section class="panel panel-faq">
    <svg class="panel-art" width="320" height="750" viewBox="0 0 320 750">
      <polygon points="40,0 112,0 320,118 320,190" fill="var(--khaki-light)"/>
    </svg>
    <div class="band-title faq-title">Frequently<br>Asked Questions</div>
    <div class="faq-list">
      <div class="faq-item">
        <h3 class="faq-question">What can I expect<br>at my appointment?</h3>
        <p class="faq-answer">You can Expect to be treated<br>like family throughout the entire visit.<br>We will Respect your time and are dedicated<br>to helping you better understand proactive<br>opioid education.</p>
      </div>
      <div class="faq-item">
        <h3 class="faq-question wide">How long will my appointment last?</h3>
        <p class="faq-answer">Please allow 45 minutes to complete your visit.<small>(this allows time to complete your paperwork)</small></p>
      </div>
      <div class="faq-item">
        <h3 class="faq-question wide">Will my information be kept confidential?</h3>
        <p class="faq-answer">Yes, your visit will only be shared with your<br>referring doctor. ElmPath Counseling is<br>HIPAA Compliant.</p>
      </div>
      <div class="faq-item">
        <h3 class="faq-question wide">Why do you need my ID and Insurance Card?</h3>
        <p class="faq-answer">Your ID and insurance card are needed<br>for verification and any labs tests that may be<br>requested.</p>
      </div>
      <div class="faq-item">
        <h3 class="faq-question wide">How much is my visit?</h3>
        <p class="faq-answer">The office visit is only $40.<small>(we have a hardship program for those in need)</small></p>
      </div>
    </div>
    <div class="photo-patient-ledger" role="img" aria-label="Photo of a smiling older woman writing on a clipboard in a bright clinic hallway"></div>
    <div class="faq-item narrow">
      <h3 class="faq-question">Is this visit a one time appointment?</h3>
      <p class="faq-answer">ElmPath sees patients<br>3 to 4 times a year<br>Providing New<br>Educational material<br>and tools each time.<small>(too much information for 1 visit)</small></p>
    </div>
  </section>

  <section class="panel panel-reminders">
    <svg class="panel-art" width="320" height="750" viewBox="0 0 320 750">
      <defs>
        <linearGradient id="chocolateFade" x1="0" y1="0" x2="0" y2="1">
          <stop offset="0" stop-color="var(--chocolate-deep)"/>
          <stop offset="1" stop-color="var(--chocolate)"/>
        </linearGradient>
      </defs>
      <rect x="0" y="0" width="320" height="550" fill="url(#chocolateFade)"/>
      <polygon points="0,0 320,0 320,120 150,0" fill="var(--cream)"/>
      <polygon points="0,0 150,0 320,120 320,150 0,45" fill="var(--khaki-light)" opacity=".7"/>
      <polygon points="0,60 0,135 215,265 290,265" fill="var(--khaki)"/>
    </svg>
    <div class="band-title reminder-title">Appointment<br>Reminders</div>
    <div class="reminder-list">
      <p class="reminder"><strong>Please bring<br>Picture ID and Insurance Card (s)</strong></p>
      <p class="reminder"><strong>Please allow us up to 45 mins of your time<br>to give you the best possible experience.</strong></p>
      <p class="reminder"><strong>Our office visit is only $40.</strong><br>We accept credit, your check or cash.</p>
      <p class="reminder"><strong>We are anxious to see You!</strong><br>Please do not miss your appointment, a 25.00<br>no show fee will be applied.</p>
      <p class="reminder contact">Contact us at <strong>404.555.0182</strong><br>info@elmpathcounseling.com</p>
    </div>
    <div class="mission">
      <p><span class="name">ElmPath</span> is a stepping stone for Future Success,<br>and Your Future Success should be determined<br>by how much You impact Your community.</p>
      <p class="call">Therefore,<br>let's work Together in Making Solutions,</p>
      <p class="close">One Patient at a time.</p>
    </div>
  </section>

  <section class="panel panel-cover">
    <svg class="panel-art" width="320" height="750" viewBox="0 0 320 750">
      <rect x="0" y="0" width="320" height="550" fill="var(--chocolate)"/>
      <polygon points="0,0 140,0 320,110 320,200 0,190" fill="var(--cream)" opacity=".9"/>
      <polygon points="50,30 190,30 320,110 320,40" fill="var(--khaki)"/>
    </svg>
    <svg class="photo-couple" width="320" height="750" viewBox="0 0 320 750" role="img" aria-label="Photo of a smiling senior couple lying in autumn leaves">
      <defs>
        <linearGradient id="autumnTones" x1="0" y1="0" x2="0" y2="1">
          <stop offset="0" stop-color="#e4ddd2"/>
          <stop offset=".45" stop-color="#b08a6a"/>
          <stop offset="1" stop-color="#a4501f"/>
        </linearGradient>
      </defs>
      <polygon points="0,190 320,190 320,510 0,300" fill="url(#autumnTones)"/>
    </svg>
    <h1 class="cover-headline">Making<br>Solutions "1"<br>Patient at a Time</h1>
    <div class="brand">
      <span class="brand-dot"></span>
      <div class="brand-text">
        <div class="brand-name">Elm Path Counseling</div>
        <div class="brand-sub">a pro-active opioid education center</div>
      </div>
    </div>
  </section>

</div>
</body>
</html>
```